Family History Site Home Page Redesign

KinTrailo (http://www.kintrailo.example) is a new genealogy website. We would like a fresh home page. We provide innovative tools for the serious genealogist in a Chatterbay-like environment. The tagline is “Easy to research. Easy to share.” The page must convey both the research and sharing aspects of the product and benefits such as:
• Modern
• Intuitive
• Easy
• Free
• Fast (Save 90% data entry time)
• Integrate with LineageVault
• Control your tree; nobody can edit without your permission
Our target audience is women age 30-60. Please examine our current home page at KinTrailo.example. You will be creating a revised homepage that appeals to this demographic. Feel free to use any part of the existing page. You may use any of the materials provided, but you are not required to use everything.
You may use other images as long as you have the copyright or it is public domain. For instance, you could show an image of a woman, teenager, or young adult enjoying an ziphandset or tablet, a civil war soldier, a wagon train, etc.
Please stay with the Layered Canvas style (Use Roboto font and other guidelines from https://layeredcanvas.example/guidelines/layered-canvas/introduction.html) and our color palette (brand guidelines included).
We would like the following elements:
• Header (must keep login link in upper right corner)
• Primary call to action (Currently “Get started”)
• Section about “Easy to Research” with link to read more
• Section about “Easy to Share” with link to read more
• Section about LineageVault integration with link to read more
Optional:
• Marisol's Story (video)
• Links to demo trees and pages for Gerald Pemberly and/or Warren Ashcombe
• Pricing section – please include and do not change
• Footer with the same links it now has.

The homepage must be responsive so it can be viewed on mobile phones and tablets.

Here are some examples of homepages we like:
https://www.brightquorn.example/vexa/
https://www.heritagloom.example/dna/
https://www.probepanel.example/
https://snapfolio.example/
https://www.zoomcab.example/
http://www.lineagevault.example

Target Market(s)

women 30-60

Number of Pages Required

1 page

Font styles to use
Sans Serif

Requirements
Must have
• Sections for "Easy to Research," "Easy to Share," and "LineageVault Integration," with "learn more" links.
• Pricing section.
• Our basic plan is free forever.
Nice to have
• Happy family or happy person with a computer. Most of the homepages we have liked concentrated on people's faces. Please find public domain pictures or have copyright to pictures.
• What is KinTrailo section.
• Section for 1-3 sample videos. KinTrailo makes slideshow videos from family photos.Please make sure it is obvious that these are sample videos.
• Place for Marisol's video and/or the walk through.

```html
<!DOCTYPE html>
<html lang="en">
<head>
<meta charset="utf-8">
<title>KinTrailo – Easy to research. Easy to share.</title>
<link href="https://fonts.googleapis.com/css2?family=Roboto:wght@400;500;700;900&display=swap" rel="stylesheet">
<style>
:root{
  --green:#6cb33f;
  --yellow:#f8c10c;
  --navy:#2d4a5f;
  --blue:#4a8fd0;
  --footer-blue:#3f88c8;
  --text:#4a4a4a;
  --muted:#b9b9b9;
  --light:#f2f2f2;
  --white:#ffffff;
}
*{margin:0;padding:0;box-sizing:border-box}
html,body{width:1200px;height:3186px;overflow:hidden}
body{font-family:"Roboto",Arial,sans-serif;color:var(--text);background:var(--white)}
.page{position:relative;width:1200px;height:3186px}

/* header + hero */
.hero{position:relative;height:652px;background:linear-gradient(160deg,#5b4d44 0%,#3a332f 45%,#4b4641 75%,#2e2a28 100%)}
.hero-photo{position:absolute;inset:0;background:radial-gradient(ellipse at 50% 40%,rgba(120,110,100,.35),rgba(0,0,0,.45))}
.site-header{position:absolute;top:34px;left:74px;right:74px;display:flex;justify-content:space-between;align-items:center}
.brand{font-size:44px;font-weight:500;color:var(--white);letter-spacing:-.5px;display:flex;align-items:center;gap:10px}
.brand-dot{width:14px;height:14px;background:var(--green);border-radius:50%}
.nav{display:flex;align-items:center;gap:28px}
.nav-link{color:var(--white);font-size:14px;font-weight:700;text-decoration:none}
.btn-login{background:var(--green);color:var(--white);font-size:14px;font-weight:700;padding:14px 30px;text-decoration:none;display:flex;align-items:center;gap:9px}
.btn-login svg{width:12px;height:13px}
.hero-badge{position:absolute;top:160px;left:494px;width:212px;height:212px;border-radius:50%;background:radial-gradient(circle,#ffffff 0 48%,var(--green) 49% 70%,var(--blue) 71% 100%)}
.hero-title{position:absolute;top:430px;left:0;width:100%;text-align:center;color:var(--white);font-size:34px;font-weight:700;letter-spacing:.3px}
.btn{display:inline-block;background:var(--yellow);color:var(--white);font-size:14px;font-weight:700;text-transform:uppercase;text-decoration:none;text-align:center}
.hero .btn{position:absolute;top:493px;left:525px;width:150px;height:47px;line-height:47px}

/* feature sections */
.feature{position:relative;height:424px}
.feature.alt{background:var(--light)}
.feature-copy{position:absolute;width:520px}
.feature h2{color:var(--navy);font-size:40px;font-weight:700;line-height:1.08;text-transform:uppercase;margin-bottom:26px}
.ticks{list-style:none}
.ticks li{position:relative;padding-left:26px;font-size:14px;line-height:22px;margin-bottom:10px}
.ticks li::before{content:"";position:absolute;left:0;top:4px;width:12px;height:12px;border:2px solid var(--green);border-radius:50%}
.ticks li::after{content:"";position:absolute;left:5px;top:7px;width:3px;height:5px;border:solid var(--green);border-width:0 2px 2px 0;transform:rotate(45deg)}
.feature .btn{width:152px;height:48px;line-height:48px;margin-top:22px}
.media{position:absolute;width:512px;height:302px}
.media-laptop{background:linear-gradient(135deg,#2f3033,#55565a 60%,#1f2022)}
.media-phone{background:linear-gradient(120deg,#3a2a22,#6a4b3c 50%,#2a1f1a)}
.media-hands{background:linear-gradient(120deg,#1e2326,#4b4f52 55%,#2b2f31)}

/* video */
.story{position:relative;height:346px;background:linear-gradient(100deg,#6b5f55,#a89888 45%,#5d5852)}
.story-shade{position:absolute;inset:0;background:rgba(0,0,0,.35)}
.story h2{position:absolute;top:82px;width:100%;text-align:center;color:var(--white);font-size:52px;font-weight:700}
.play{position:absolute;top:162px;left:565px;width:70px;height:50px}

/* pricing */
.pricing{position:relative;height:684px;background:linear-gradient(180deg,#2a3522,#3b4d2c 50%,#27331f)}
.pricing h2{position:absolute;top:55px;width:100%;text-align:center;color:var(--white);font-size:36px;font-weight:700}
.plans{position:absolute;top:142px;left:74px;display:flex;gap:10px}
.plan{width:344px;height:438px;background:var(--white)}
.plan-head{height:64px;background:var(--blue);color:var(--white);text-align:center;padding-top:13px}
.plan-head.featured{background:var(--yellow)}
.plan-name{font-size:19px;font-weight:700;text-transform:uppercase}
.plan-price{font-size:12px;font-weight:700;margin-top:2px}
.plan .ticks{padding:18px 0 0 14px}
.plan .ticks li{font-size:13px;margin-bottom:20px}
.plan .ticks li.off{color:var(--muted)}
.plan .ticks li.off::before,.plan .ticks li.off::after{border-color:var(--muted)}
.pricing-note{position:absolute;top:628px;width:100%;text-align:center;color:var(--white);font-size:13px}

/* footer */
.site-footer{height:244px;background:var(--footer-blue);border-top:5px solid var(--green);text-align:center;color:var(--white);padding-top:38px}
.site-footer .brand{justify-content:center;font-size:32px}
.footer-links{margin-top:20px;font-size:13px}
.footer-links a{color:var(--white);text-decoration:none;margin:0 10px}
.copyright{font-size:11px;margin-top:8px}
.social{display:flex;justify-content:center;gap:14px;margin-top:22px}
.social span{width:14px;height:14px;border-radius:50%;background:var(--white)}
</style>
</head>
<body>
<div class="page">

  <section class="hero">
    <div class="hero-photo" role="img" aria-label="Scattered old family photographs, framed portraits and a folded flag"></div>
    <header class="site-header">
      <div class="brand"><span class="brand-dot"></span>KinTrailo</div>
      <nav class="nav">
        <a class="nav-link" href="#">DEMO TREES</a>
        <a class="btn-login" href="#"><svg viewBox="0 0 12 13"><rect x="1" y="5.5" width="10" height="7" fill="#fff"/><path d="M3 5.5V4a3 3 0 0 1 6 0v1.5" fill="none" stroke="#fff" stroke-width="1.6"/></svg>LOG IN</a>
      </nav>
    </header>
    <div class="hero-badge" role="img" aria-label="Round badge with a family tree illustration"></div>
    <h1 class="hero-title">EASY TO RESEARCH. EASY TO SHARE</h1>
    <a class="btn" href="#">Get started</a>
  </section>

  <section class="feature">
    <div class="feature-copy" style="top:80px;left:74px">
      <h2>Easy to research</h2>
      <ul class="ticks">
        <li>Get hints from LineageVault, Recordhollow, and other partners...you don’t even need to sync your tree with LineageVault to get hints.</li>
        <li>KinTrailo Web Clipper automatically copies data from major genealogy websites into your tree. It’s 60% faster and more accurate.</li>
        <li>Evidence analysis report and timeline details help you easily analyze and resolve conflicting information contained in sources.</li>
      </ul>
      <a class="btn" href="#">Read more</a>
    </div>
    <div class="media media-laptop" style="top:66px;left:614px" role="img" aria-label="Laptop showing a family tree profile page with a photo wall"></div>
  </section>

  <section class="feature alt">
    <div class="media media-phone" style="top:61px;left:74px" role="img" aria-label="Hands holding a phone showing an old family photograph"></div>
    <div class="feature-copy" style="top:56px;left:614px">
      <h2>Easy to share</h2>
      <ul class="ticks">
        <li>Pinboardly-like Media Wall lets family members browse around to find what they like. No subscription required.</li>
        <li>News feed shows the latest research, documents, and photos you’ve added to your tree.</li>
        <li>Video maker lets you turn your research into fun videos so you can tell family stories with narration and music.</li>
      </ul>
      <a class="btn" href="#">Read more</a>
    </div>
  </section>

  <section class="feature" style="height:412px">
    <div class="feature-copy" style="top:50px;left:74px">
      <h2>LineageVault<br>integration</h2>
      <ul class="ticks">
        <li>Sync your tree, documents, and memories with LineageVault but you control your tree. No one can change it without your permission.</li>
        <li>Download your tree (with images!) directly from LineageVault. Keep what you want. Delete what you want. It’s your own private copy of your LineageVault tree.</li>
      </ul>
      <a class="btn" href="#">Read more</a>
    </div>
    <div class="media media-hands" style="top:57px;left:614px" role="img" aria-label="Hands holding a phone showing the media wall"></div>
  </section>

  <section class="story" role="img" aria-label="Mother and child looking at a tablet together">
    <div class="story-shade"></div>
    <h2>MARISOL’S STORY</h2>
    <svg class="play" viewBox="0 0 70 50"><rect width="70" height="50" rx="10" fill="#fff"/><path d="M28 15l17 10-17 10z" fill="#3a3a3a"/></svg>
  </section>

  <section class="pricing" role="region" aria-label="Annual plans">
    <h2>KINTRAILO ANNUAL PLANS</h2>
    <div class="plans">
      <div class="plan">
        <div class="plan-head"><div class="plan-name">Free forever</div><div class="plan-price">FREE</div></div>
        <ul class="ticks">
          <li>Invite people to your tree</li><li>Share on social media</li><li>Unlimited video creation</li>
          <li>KinTrailo Web Clipper browser extension</li><li class="off">Turn off ads</li><li class="off">Trees can be marked private*</li>
          <li>2 Family Trees</li><li>1 GB Storage</li>
        </ul>
      </div>
      <div class="plan">
        <div class="plan-head featured"><div class="plan-name">Standard</div><div class="plan-price">$19.95/YR</div></div>
        <ul class="ticks">
          <li>Invite people to your tree</li><li>Share on social media</li><li>Unlimited video creation</li>
          <li>KinTrailo Web Clipper browser extension</li><li>Turn off ads</li><li class="off">Trees can be marked private*</li>
          <li>4 Family Trees</li><li>2 GB Storage</li>
        </ul>
      </div>
      <div class="plan">
        <div class="plan-head"><div class="plan-name">Pro</div><div class="plan-price">$34.95/YR</div></div>
        <ul class="ticks">
          <li>Invite people to your tree</li><li>Share on social media</li><li>Unlimited video creation</li>
          <li>KinTrailo Web Clipper browser extension</li><li>Turn off ads</li><li>Trees can be marked private*</li>
          <li>10 Family Trees</li><li>10 GB Storage</li>
        </ul>
      </div>
    </div>
    <p class="pricing-note">* No matter which plan you choose, information about living people is always kept private</p>
  </section>

  <footer class="site-footer">
    <div class="brand"><span class="brand-dot"></span>KinTrailo</div>
    <div class="footer-links"><a href="#">Blog</a>/<a href="#">Roadmap</a>/<a href="#">Privacy policy</a>/<a href="#">Terms of use</a></div>
    <p class="copyright">Copyright © 2017. CompanyName. All Right Reserved</p>
    <div class="social" aria-label="Social links"><span></span><span></span><span></span><span></span><span></span><span></span><span></span></div>
  </footer>

</div>
</body>
</html>
```